Copperfield interiors PTY LTD

My business specializes in commercial fitout which builds walls, ceilings, doors, uses also materials aluminium in works. Id like to have a logo designed for my company too.

Industry/Entity Type

Business

```html
<!DOCTYPE html>
<html lang="en">
<head>
<meta charset="utf-8">
<title>Copperfield interiors PTY LTD — Business Card</title>
<link href="https://fonts.googleapis.com/css2?family=Questrial&display=swap" rel="stylesheet">
<style>
  :root {
    --navy: #050a1f;
    --brand-blue: #1f80c1;
    --slate: #5f6b74;
    --ink: #14161c;
    --paper: #f4f4f2;
    --wave-tint: #dbe9f1;
    --backdrop: #a9aaab;
  }
  * { margin: 0; padding: 0; box-sizing: border-box; }
  html, body { width: 1200px; height: 1200px; overflow: hidden; }
  body {
    background: var(--backdrop);
    font-family: "Questrial", "Century Gothic", sans-serif;
    position: relative;
  }
  .card {
    position: absolute;
    left: 170px;
    width: 860px;
    height: 490px;
    overflow: hidden;
    box-shadow: 0 6px 18px rgba(0,0,0,0.18);
  }
  .card--front { top: 80px; background: var(--navy); }
  .card--back  { top: 630px; background: var(--paper); }

  .wordmark { position: absolute; display: flex; align-items: center; gap: 22px; }
  .wordmark__dot {
    border-radius: 50%;
    border: 3px solid currentColor;
    flex: none;
  }
  .wordmark__name { color: var(--brand-blue); line-height: 1; letter-spacing: 1px; }
  .wordmark__sub { line-height: 1.1; letter-spacing: 1px; margin-top: 6px; }

  .card--front .wordmark { left: 150px; top: 175px; color: #ffffff; }
  .card--front .wordmark__dot { width: 96px; height: 96px; }
  .card--front .wordmark__name { font-size: 64px; }
  .card--front .wordmark__sub { font-size: 36px; color: #ffffff; }

  .card--back .wordmark { left: 40px; top: 70px; color: var(--slate); }
  .card--back .wordmark__dot { width: 62px; height: 62px; }
  .card--back .wordmark__name { font-size: 42px; }
  .card--back .wordmark__sub { font-size: 24px; color: var(--slate); }

  .card__decor { position: absolute; inset: 0; }

  .person { position: absolute; right: 50px; top: 100px; text-align: right; color: var(--ink); }
  .person__name { font-size: 30px; letter-spacing: 1px; }
  .person__title { font-size: 18px; margin-top: 4px; }

  .contact {
    position: absolute; left: 430px; top: 215px;
    list-style: none; font-size: 18px; color: var(--ink); line-height: 1.35;
  }
  .contact li { display: flex; }
  .contact__label { width: 30px; flex: none; }
</style>
</head>
<body>

  <section class="card card--front" aria-label="Card front">
    <div class="wordmark">
      <span class="wordmark__dot"></span>
      <div>
        <div class="wordmark__name">Copperfield</div>
        <div class="wordmark__sub">interiors PTY LTD</div>
      </div>
    </div>
  </section>

  <section class="card card--back" aria-label="Card back">
    <svg class="card__decor" viewBox="0 0 860 490" width="860" height="490">
      <circle role="img" aria-label="Soft brand backdrop shape" cx="620" cy="330" r="225" fill="var(--wave-tint)"/>
      <path d="M0 315 L60 318 L560 440 L860 440 L860 490 L0 490 Z" fill="var(--navy)"/>
      <path d="M90 322 L250 335 L620 432 L520 426 Z" fill="var(--brand-blue)"/>
    </svg>

    <div class="wordmark">
      <span class="wordmark__dot"></span>
      <div>
        <div class="wordmark__name">Copperfield</div>
        <div class="wordmark__sub">interiors PTY LTD</div>
      </div>
    </div>

    <div class="person">
      <div class="person__name">Your Full Name</div>
      <div class="person__title">Your Tittle</div>
    </div>

    <ul class="contact">
      <li><span class="contact__label">A</span><span>: Your address line 1<br>&nbsp;&nbsp;Your address line 2</span></li>
      <li><span class="contact__label">P</span><span>: 012.345.6789</span></li>
      <li><span class="contact__label">E</span><span>: Your email@yourdomain.com</span></li>
      <li><span class="contact__label">W</span><span>: www.yourdomain.com</span></li>
    </ul>
  </section>

</body>
</html>
```